plume: nature's odor eliminator

I need a label design for a chemical free air freshener/odor eliminator. The product is "Plume: Odor Eliminator"

I want to keep the design simple and eco friendly themed. (green/blue color theme) I have attached some sketches and mockups ive created. the bottle is a transparent blue, so i would like the main logo to be in green, and the lettering we can try different colors to see what stands out. I would like the label to be designed with a clear label to use the blue background of the bottle.

Contains No Chemicals
Readily biodegradable
Phosphate-free
Non-toxic, non-corrosive and environmentally-friendly
Made with essential oils.

Safe to use around kids, plants and pets.

Elliminates odors, including:
Smoke odors: ( tobacco, medical marijuana, fire)
Vomit
Urine
Gasoline

Replaces toxic air fresheners.

Ingredients: Distilled Water, Proprietary Odor Eliminating Enzyme Blend, Proprietary Essential Oil Blend.

I will be using this bottle:
http://www.vesselsupplyhub.example/item/K842

Label Dimensions: 5.6875 x 5 in

Target Market(s)

People who use air fresheners (aireluxe or mistra) and want an alternative that does not have toxic chemicals.

Requirements
Must have
• Bold green main lettering

```html
<!DOCTYPE html>
<html lang="en">
<head>
<meta charset="utf-8">
<title>Plume: Odor Eliminator label</title>
<link href="https://fonts.googleapis.com/css2?family=Jost:wght@300;400;500;700&display=swap" rel="stylesheet">
<style>
  :root {
    --page: #ffffff;
    --ink: #ffffff;
    --brand-green: #46c94a;
    --label-top: #0b0e55;
    --label-deep: #0712c4;
    --label-mid: #1d4fdc;
    --label-light: #2a70e2;
    --label-bottom: #1434d2;
  }
  html, body {
    margin: 0;
    padding: 0;
    width: 1200px;
    height: 1000px;
    overflow: hidden;
    background: var(--page);
  }
  .canvas {
    position: relative;
    width: 1200px;
    height: 1000px;
    background: var(--page);
  }
  .label {
    position: absolute;
    left: 402px;
    top: 295px;
    width: 360px;
    height: 413px;
    overflow: hidden;
    background: linear-gradient(180deg,
      var(--label-top) 0%,
      var(--label-deep) 24%,
      var(--label-mid) 55%,
      var(--label-light) 78%,
      var(--label-bottom) 100%);
    color: var(--ink);
    font-family: "Jost", "Futura", sans-serif;
    text-transform: uppercase;
  }
  .label > * {
    position: absolute;
    left: 8px;
    margin: 0;
    white-space: nowrap;
    line-height: 1;
  }
  .brand-name {
    top: 6px;
    left: 9px;
    font-size: 74px;
    font-weight: 700;
    color: var(--brand-green);
    text-transform: none;
  }
  .tagline {
    top: 111px;
    font-size: 26.5px;
    font-weight: 300;
  }
  .tagline-call {
    top: 143px;
    font-size: 22px;
    font-weight: 700;
    letter-spacing: 1px;
  }
  .odor-list {
    top: 180px;
    font-size: 15.8px;
    font-weight: 400;
    line-height: 18px;
  }
  .odor-list strong {
    font-weight: 700;
    font-size: 16.4px;
    letter-spacing: 0.4px;
  }
  .safety {
    top: 233px;
    font-size: 14.2px;
    font-weight: 400;
  }
  .properties {
    top: 263px;
    font-size: 11.6px;
    font-weight: 700;
    letter-spacing: -0.2px;
  }
  .instructions {
    top: 291px;
    font-size: 14.5px;
    font-weight: 500;
    line-height: 17px;
    letter-spacing: 0.4px;
  }
  .eco-claim {
    top: 343px;
    font-size: 16px;
    font-weight: 700;
    letter-spacing: -0.3px;
  }
  .fine-print {
    top: 376px;
    font-size: 8.9px;
    font-weight: 700;
    line-height: 12px;
  }
</style>
</head>
<body>
  <main class="canvas">
    <section class="label" aria-label="Plume odor eliminator label">
      <h1 class="brand-name">plume</h1>
      <p class="tagline">Don’t cover up the odor</p>
      <p class="tagline-call">Plume it!</p>
      <p class="odor-list">Destroys odors from: medical marijuana,<br><strong>Cigarette smoke,cooking casoline</strong></p>
      <p class="safety">Safe to use around humans, animals &amp; plants</p>
      <p class="properties">Non-toxic, biodegrable, non-staining, non-corrosive</p>
      <p class="instructions">Instructions:&nbsp; spray liberally and high as<br>possible in room and on source of odor</p>
      <p class="eco-claim">Eco-friendly, no CFC’s, no phosphates</p>
      <p class="fine-print">Doesn’t contain neurotoxins or ingredients linked to cancer<br>and birth deffects. Unliket the l-eading brands of air fresheners.</p>
    </section>
  </main>
</body>
</html>
```